Web Design Project

Brightwater Digital owns and operates a large number of editorial websites. These websites provides mostly consumers in the financial services space with information and price comparisons for a particular service.

Brightwater Digital, as the holding company for each of these sites, currently has no website. We need to build a website targeted towards potential partners for our websites. The idea being that when we start a conversation with a partner, they can view our site and obtain some basic information about who we are.

The structure of the site is to be very simple, containing only a brief description about who we are, our contact details and a list of some of our websites:
• CoverQuest.net.au
• AutoPolicyMatcher.com.au
• NestPolicyMatcher.com.au
• WellPolicyMatcher.com.au
• CoverQuestMatcher.com.au
• TripPolicyMatcher.com.au
• CritterPolicyMatcher.com.au
• CashAdvanceMatcher.com.au
• MobileCoolingUnit.com.au
• FixedSaverYields.com.au
• ThriftyHabits.com.au
• PurseGran.com.au
• TameThePlastic.com.au
• PurseMinder.com.au
• ThirdPartyClaimsCoverOzland.com.au
• Trade-Protect.com.au
• AutoPolicyProviders.com.au
• WellPolicyProviders.com.au
• NestPolicyOzland.com
• CoverQuestOzland.com
• WageShieldPolicyOzland.com
• WellPolicyOzland.com
• CritterPolicyOzland.com
• CashAdvancesOzland.com
• PlasticPaysOzland.com
• NestLendersOzland.com
• NestEggFunds.net.au

The design of the site should say 'Internet company', 'professional', 'fresh thinking'. The design should not look like a corporate site that you would see from any corporate services business with images of people in suits. We are ultimately an Internet business and there should be a unique feel to the site.

We are open to a suggestion of a colour pallet as the holding company does not have an established logo.

Some sites that we like are:

http://www.prismwork-studio.co.uk/#home
http://sample00.layoutvault.example/wt_48248/index.html
http://sample00.layoutvault.example/wordpress_46388/
http://mindvolt.example/
http://www.tandora.us/
http://www.kelvorabintu.example/
http://www.slickfrontpages.example/Corporate/design-ideas-detail.html?id=7916
http://trebla.example/
http://orvantek.example/

Reason: Hi all, Apologies, but I need to extend the timeline. One of our key stakeholders is away for the next week. There are a few good designs that we have received to date and there are some tweaks that we would like to see before making a final decision. Thank you to everyone that has submitted designs - Have a great new year. Derek

Reason: Sorry to have to delay the deadline on this, but we did not find anything in the designs really resonated with us. We will have a further think about the existing designs that have been submitted and how we can provide more specific feedback to the designers to make some modifications to the designs.

Target Market(s)

We are targeting insurance companies / brokers that we are talking to. The idea is that we show a professional face to them.

Industry/Entity Type

Financial

Requirements
Must have
• Home Page (possibly integrated with About us details)
Contact Us
Our Sites

```html
<!DOCTYPE html>
<html lang="en">
<head>
<meta charset="utf-8">
<title>Brightwater Digital</title>
<link rel="stylesheet" href="https://fonts.googleapis.com/css2?family=Arimo:wght@400;700&family=Roboto:wght@300;400&family=Gelasio&display=swap">
<style>
:root{
  --page-bg:#e4ddd3;
  --stripe:#d9d1c5;
  --header:#4f4641;
  --nav:#d8c9b3;
  --white:#ffffff;
  --ink:#3a3330;
  --sand:#f2e2cf;
  --panel:#ececec;
  --panel-line:#c9c9c9;
  --title-blue:#58698a;
  --social-blue:#3b5998;
  --link-blue:#3b5998;
  --footer-top:#6a6a6a;
  --footer-bot:#1d1d1d;
}
*{box-sizing:border-box;margin:0;padding:0}
html,body{width:1200px;height:750px;overflow:hidden}
body{
  background:repeating-linear-gradient(180deg,var(--page-bg) 0 3px,var(--stripe) 3px 4px);
  font-family:'Arimo',Arial,sans-serif;color:var(--ink);position:relative;
}
.page{position:absolute;left:176px;top:0;width:833px;height:750px;background:var(--white);box-shadow:0 0 8px rgba(0,0,0,.25)}
.site-header{position:absolute;left:0;top:0;width:833px;height:74px;background:var(--header)}
.brand{position:absolute;left:41px;top:10px;font-family:'Roboto',sans-serif;font-weight:300;font-size:30px;color:#fff;letter-spacing:-.2px;white-space:nowrap}
.main-nav{position:absolute;right:45px;top:41px;font-family:'Roboto',sans-serif;font-size:17px;color:var(--nav);white-space:nowrap}
.main-nav a{color:var(--nav);text-decoration:none}
.main-nav a.current{color:#fff}
.main-nav .sep{margin:0 4px}

.hero{position:absolute;left:41px;top:83px;width:750px;height:250px;overflow:hidden;box-shadow:0 6px 8px -4px rgba(0,0,0,.25)}
.hero-photo{position:absolute;inset:0;background:linear-gradient(90deg,var(--sand) 0%,var(--sand) 36%,#d7bc9f 50%,#a88865 62%,#7d6147 75%,#caa98a 88%,#b39275 100%)}
.hero-title{position:absolute;left:15px;top:5px;font-family:'Roboto',sans-serif;font-weight:300;font-size:23.5px;color:#2c2622;white-space:nowrap}
.hero-text{position:absolute;left:17px;top:44px;width:225px;font-family:'Roboto',sans-serif;font-weight:300;font-size:13.4px;line-height:20px;color:#6b5f55}
.btn{position:absolute;height:19px;border-radius:4px;background:linear-gradient(#d8d8d8,#a9a9a9);border:1px solid #8d8d8d;font-size:9.5px;color:#333;line-height:17px;padding-left:6px;white-space:nowrap;text-decoration:none}
.btn svg{position:absolute;right:4px;top:4px}
.btn-dark{background:linear-gradient(#7b7068,#544a43);border-color:#3f3732;color:#f2ece6}
.hero .btn{left:180px;top:214px;width:74px}
.slider-dots{position:absolute;left:364px;top:342px;display:flex;gap:4px}
.slider-dots span{width:9.5px;height:9.5px;border-radius:50%;background:#a6a6a6}
.slider-dots span.on{background:radial-gradient(circle at 40% 35%,#a0785a,#3d2a1d)}

.sites-panel{position:absolute;left:42px;top:363px;width:234px;height:314px;background:var(--panel);border:1px solid var(--panel-line);box-shadow:3px 4px 5px rgba(0,0,0,.18)}
.sites-panel h2{position:absolute;left:12px;top:7px;font-family:'Roboto',sans-serif;font-weight:400;font-size:20px;color:#222}
.site-list{position:absolute;left:15px;top:38px;width:207px;list-style:none;border-top:1px solid #d0d0d0}
.site-list li{height:24.2px;border-bottom:1px solid #d0d0d0;box-shadow:0 1px 0 #fff;font-size:10px;color:#555;line-height:23px;padding-left:29px;position:relative;letter-spacing:.2px;white-space:nowrap}
.site-list li::before{content:"";position:absolute;left:12px;top:9px;width:4px;height:4px;border-right:1.5px solid #333;border-top:1.5px solid #333;transform:rotate(45deg)}
.sites-panel .btn{left:129px;top:286px;width:90px;padding-left:9px}

.about{position:absolute;left:302px;top:363px;width:225px}
.about h1{font-family:'Gelasio',Georgia,serif;font-weight:400;font-size:21.5px;color:var(--title-blue);padding-bottom:4px;border-bottom:1px solid #ddd;white-space:nowrap}
.about p{font-size:10px;line-height:16.7px;color:#333;margin-top:10px}
.about p + p{margin-top:15px}
.about-more{left:444px;top:654px;width:74px}

.social-box{position:absolute;left:549px;top:364px;width:242px;height:246px;border:1px solid #a9b3c8}
.social-head{height:27px;background:var(--social-blue);color:#fff;font-size:10.5px;line-height:27px;padding-left:8px}
.page-badge{position:absolute;left:9px;top:37px;width:33px;height:33px;background:#ececec;border:1px solid #ddd}
.page-name{position:absolute;left:50px;top:35px;font-size:12.5px;font-weight:700;color:var(--link-blue);letter-spacing:.3px}
.like-btn{position:absolute;left:51px;top:54px;width:38px;height:19px;border:1px solid #c4cde0;background:#eef1f7;border-radius:2px;font-size:9px;color:var(--link-blue);line-height:17px;padding-left:17px}
.like-btn svg{position:absolute;left:4px;top:3px}
.fans-count{position:absolute;left:9px;top:94px;font-size:9px;color:#333;white-space:nowrap}
.fans-count b{font-size:10.5px;letter-spacing:.3px}
.fans{position:absolute;left:9px;top:107px;display:grid;grid-template-columns:repeat(5,42px);column-gap:4px;row-gap:8px}
.fan{width:42px;text-align:center;font-size:7.5px;color:#666}
.fan .pic{width:42px;height:42px;margin-bottom:5px}
.plugin-foot{position:absolute;left:7px;top:227px;width:227px;border-top:1px solid #ccc;padding-top:4px;font-size:8px;color:#666;padding-left:15px}
.plugin-foot::before{content:"";position:absolute;left:0;top:5px;width:11px;height:11px;background:var(--social-blue)}

.share-icons{position:absolute;left:674px;top:679px;display:flex;gap:4px}
.share-icons span{width:25px;height:25px;border-radius:4px}

.site-footer{position:absolute;left:0;top:720px;width:833px;height:30px;background:linear-gradient(var(--footer-top),#3a3a3a 40%,var(--footer-bot));color:#eee;font-size:8.5px;line-height:30px}
.site-footer .copy{position:absolute;left:25px}
.site-footer .credit{position:absolute;right:25px}
</style>
</head>
<body>
<div class="page">
  <header class="site-header">
    <div class="brand">Brightwater Digital</div>
    <nav class="main-nav">
      <a class="current" href="#">Home</a><span class="sep">|</span><a href="#">Our Sites</a><span class="sep">|</span><a href="#">About</a><span class="sep">|</span><a href="#">Contat Us</a>
    </nav>
  </header>

  <section class="hero">
    <div class="hero-photo" role="img" aria-label="Sepia-toned photo of a businesswoman holding folders with colleagues blurred behind her"></div>
    <h2 class="hero-title">Lorem Ipsum is simply dummy text</h2>
    <p class="hero-text">Lorem Ipsum is simply dummy text of the printing and typesetting industry. Lorem Ipsum has been the industry's standard dummy text ever since the 1500s, when an unknown printer took a galley of type and scrambled it to make a type specimen book.</p>
    <a class="btn btn-dark">Read More<svg width="9" height="9"><path d="M0 0 L9 4.5 L0 9Z" fill="#fff"/></svg></a>
  </section>
  <div class="slider-dots"><span></span><span class="on"></span><span></span><span></span><span></span><span></span><span></span><span></span></div>

  <aside class="sites-panel">
    <h2>Our Sites</h2>
    <ul class="site-list">
      <li>CoverQuest.net.au</li>
      <li>AutoPolicyMatcher.com.au</li>
      <li>NestPolicyMatcher.com.au</li>
      <li>WellPolicyMatcher.com.au</li>
      <li>CoverQuestMatcher.com.au</li>
      <li>TripPolicyMatcher.com.au</li>
      <li>CritterPolicyMatcher.com.au</li>
      <li>CashAdvanceMatcher.com.au</li>
      <li>MobileCoolingUnit.com.au</li>
      <li>FixedSaverYields.com.au</li>
    </ul>
    <a class="btn">View All Sites<svg width="9" height="9"><path d="M0.5 0.5 L8.5 4.5 L0.5 8.5Z" fill="#eee" stroke="#888"/></svg></a>
  </aside>

  <section class="about">
    <h1>Brightwater Digital</h1>
    <p>Lorem Ipsum is simply dummy text of the printing and typesetting industry. Lorem Ipsum has been the industry's standard dummy text ever since the 1500s, when an unknown printer took a galley of type and scrambled it to make a type specimen book. It has survived not only five centuries, but also the leap into electronic typesetting, remaining essentially unchanged.</p>
    <p>It was popularised in the 1960s with the release of Stenfold sheets containing Lorem Ipsum passages, and more recently with desktop publishing software like Orrin PageForge including versions of Lorem Ipsum.</p>
  </section>
  <a class="btn about-more">Read More<svg width="9" height="9"><path d="M0.5 0.5 L8.5 4.5 L0.5 8.5Z" fill="#eee" stroke="#888"/></svg></a>

  <aside class="social-box">
    <div class="social-head">Find us on Friendspace</div>
    <div class="page-badge"></div>
    <div class="page-name">Brightwater Digital</div>
    <div class="like-btn"><svg width="10" height="10"><path d="M1 4h2v6H1zM4 4l2-4c1 0 1.5 1 1 3h3v3l-2 4H4z" fill="#3b5998"/></svg>Like</div>
    <div class="fans-count">106 people like <b>Brightwater Digital</b></div>
    <div class="fans">
      <div class="fan"><div class="pic" role="img" aria-label="Member photo" style="background:#7d8a5a"></div>Rosalind</div>
      <div class="fan"><div class="pic" role="img" aria-label="Member photo" style="background:#8a6048"></div>Mette</div>
      <div class="fan"><div class="pic" role="img" aria-label="Member avatar" style="background:#d9a57e"></div>Osric</div>
      <div class="fan"><div class="pic" role="img" aria-label="Member photo" style="background:#a08a74"></div>Ilse</div>
      <div class="fan"><div class="pic" role="img" aria-label="Member photo" style="background:#b8563a"></div>Corinna</div>
      <div class="fan"><div class="pic" role="img" aria-label="Member photo" style="background:#8c8680"></div>Verity</div>
      <div class="fan"><div class="pic" role="img" aria-label="Member photo" style="background:#4a3a26"></div>Tamsin</div>
      <div class="fan"><div class="pic" role="img" aria-label="Member photo" style="background:#b8826a"></div>Philippa</div>
      <div class="fan"><div class="pic" role="img" aria-label="Member photo" style="background:#6c5a8a"></div>Ravena</div>
      <div class="fan"><div class="pic" role="img" aria-label="Member photo" style="background:#5e4538"></div>Soraya</div>
    </div>
    <div class="plugin-foot">Friendspace social plugin</div>
  </aside>

  <div class="share-icons">
    <span style="background:#3b5998"></span>
    <span style="background:#4fb4e6"></span>
    <span style="background:#e6e6e6"></span>
    <span style="background:#f0922c"></span>
  </div>

  <footer class="site-footer">
    <span class="copy">© Brightwater Digital 2011. All rights reserved.</span>
    <span class="credit">Powered by loomcraft.example</span>
  </footer>
</div>
</body>
</html>
```